Fenwick and Torrance Postcard Design

Greetings!
Lawyers hire me as an expert witness. They take a gamble on hiring me in hopes of winning their case.
This postcard will be printed in jumbo size through Quillmark. The design must meet these specifications:

Full Bleed Size (starting document size)
11.12" x 6.12"
282 x 155 mm
3335 x 1835 pixels
* Finished artwork should use the full bleed dimensions for best results.
Document Trim Size (final size after being cut)
11.00" x 6.00"
279 x 152 mm
3300 x 1800 pixels
* Please be sure to keep all text and photos within the safe cutting margin.
Resolution
300 DPI
Visit Quillmark for more details or to download a design template:
https://www.quillmark-example.com/product-presentation-info.aspx?productPresentationId=1590#
https://www.quillmark-example.com/vp/ns/propath/UploadResources.aspx?selectedTab=0?pfid=BDW&pf_id=BDW&xnav=product-page#FileFormats

1. The postcard will have a Blank Backside.
2. I like a black, white and red color theme with a serious legalistic font.
3. In regards to color theme, see https://www.cardorbit-example.com/designs/security-system-postcards/#security-system-postcards-4
4. 8 preferred background images in alphabetical order from favorite to least favorite, but all are great:
a. https://files.driftbox-example.com/f/s!QwErTy12ZxCvBn34MnBvCx56LkJhGf
5. Header Text:
a. (line 1) Dr. K.R. Torrance, Psy.D., NCEB
b. (lines 2 and 3) Psychological Evaluator, Board-Certified Forensic Psychologist and National Expert Witness
c. (Line 4 in bold and more prominent than text in lines 1-3) 4 Signs of a Proficient & Credible Psyc. Expert
6. View this checklist image for inspiration, https://lnk.tidepoint-example.com/images/8RqWm3 and use the following text within such a checklist image:
7. Board Certified by the Continental Council of Courtroom Behavioral Science (CCCB)?
Yes, I'm Board Certified. This mark of proficiency in forensic psychology is recognized by judicial decisions, statutes and regulations.
8. Fellow of the Cont. Fellowship of Legal Behavioral Study?
Yes, I'm a CFLB Fellow, along with some of the field's most prominent leaders comprising the academic arm of the CCCB.
9. A Recognized Leader Amongst Other Experts?
I’m the 2018 duly elected President of the Hudson Valley Behavioral Guild Section on Courtroom Assessment, and a Board Member of the Coalition of Practitioners for Youth Safeguarding.
10. Positioned in Roles of Trust and Neutrality by Judges?
Yes, I work as an in-house Harborview Juvenile Tribunal mental-health expert in proceedings regarding competency, imminent risk, sentencing, custody, child maltreatment and TPR.
11. The following should be prominent along the bottom:
12. BOOK A LUNCH & LEARN AT YOUR OFFICE
Visit http://offer.witnessbench-example.com Call 555-014-2937
Designer: This call to action (CTA) for #12 needs to pop off of the page. It needs to draw the reader's eye. It needs depth, like the way a CTA button looks like on a website. Play around w/ idea to accomplish this (e.g., adding badges, icons, shapes, a picture, an image of someone presenting it, etc).
13. List my areas of specialization somewhere
• CPS & Matrimonial Issues
• Competency
• Juvenile Delinquency
• Criminal Sentencing
• Personal Injury and Civil Rights
• Immigration
• Fitness for Duty, SSD and Workers Comp
• Sex-Offenders
• IME and Neuropsychological Testing
• Behind-The-Scenes Consulting on A Contingency Fee
• Low-Price Initial Screening Evaluations
• Therapy Services & Programs for Litigants
14. Put this test somewhere and keep it subtle: I recognize the importance of your work. You can trust my assistance.
15. Put this in fine print somewhere (can be 2 lines): Fenwick and Torrance, LLC. 2018 New York Licensed Psychologist Lic. # 047213 - New Jersey Licensed Psychologist Lic. # 72K900315847

Target Market(s)

Lawyers

Industry/Entity Type

Hire

Font styles to use
Serif

Colors
ec1f27
ffffff

Requirements
Must have
• An awesome call to action. If the CTA doesn't catch the eye, then it won't work. The point of this postcard is to get them to that website so I can capture their email address. Anything else is a secondary gain. Consider 3-d design elements to give it pop and depth.
Should not have
• There's a big difference between a red rectangle and a red button on a website that has that 3d quality. This postcard has a lot of words. It can easily become just a bunch of text on a colorful piece of paper w/ a pic. Avoid this by segmenting the space, layering Diff color text on Diff color background and incorporating 3d design elements and shapes.

```html
<!DOCTYPE html>
<html lang="en">
<head>
<meta charset="utf-8">
<title>Fenwick and Torrance Postcard</title>
<link rel="stylesheet" href="https://fonts.googleapis.com/css2?family=Montserrat:ital,wght@0,400;0,500;0,600;0,700;1,400;1,500&display=swap">
<style>
  :root {
    --red: #ec1f27;
    --white: #ffffff;
    --black: #050505;
    --ink: #1a1a1a;
    --page: #e6e6e6;
    --wood-dark: #3a1a0c;
    --wood-mid: #7a3a1c;
    --wood-light: #b07040;
  }
  * { margin: 0; padding: 0; box-sizing: border-box; }
  html, body { width: 1200px; height: 1000px; overflow: hidden; }
  body {
    background: var(--page);
    font-family: "Montserrat", Arial, sans-serif;
    position: relative;
  }
  .postcard {
    position: absolute;
    left: 66px; top: 209px;
    width: 1077px; height: 593px;
    background: var(--black);
    overflow: hidden;
  }
  .courtroom-photo {
    position: absolute; left: 0; top: 0;
    width: 1077px; height: 328px;
    background:
      radial-gradient(ellipse at 85% 40%, rgba(160,140,110,.55), transparent 45%),
      linear-gradient(180deg, #8a5a2e 0%, #6a2e18 30%, var(--wood-mid) 55%, var(--wood-dark) 100%);
  }
  .title-box {
    position: absolute; left: 42px; top: 34px;
    width: 455px; height: 102px;
    background: rgba(10,6,4,.78);
    border: 1px solid var(--red);
    padding: 14px 18px;
    color: var(--white);
  }
  .title-box h1 {
    font-size: 24px; font-weight: 600; letter-spacing: .2px; line-height: 1.15;
  }
  .title-box p {
    margin-top: 8px; font-size: 15px; font-weight: 500; line-height: 1.3;
  }
  .signs {
    position: absolute; left: 0; top: 328px;
    width: 747px; height: 224px;
    background: var(--black);
    padding: 14px 18px 0 21px;
    color: var(--white);
  }
  .signs h2 {
    color: var(--red); font-size: 15px; font-weight: 700; margin-bottom: 9px;
  }
  .sign {
    display: flex; gap: 7px;
    font-size: 11.4px; line-height: 1.42; margin-bottom: 10px;
  }
  .sign svg { flex: none; width: 10px; height: 10px; margin-top: 3px; }
  .sign strong { font-weight: 600; }
  .sign em { font-style: italic; font-weight: 400; }
  .cta-bar {
    position: absolute; left: 0; top: 552px;
    width: 747px; height: 41px;
    background: var(--white);
    display: flex; align-items: center; justify-content: center;
    font-size: 20px; font-weight: 600; color: var(--ink);
  }
  .cta-bar .accent { color: var(--red); margin: 0 6px; }
  .specialization {
    position: absolute; left: 747px; top: 228px;
    width: 330px; height: 365px;
    background: var(--red);
    color: var(--white);
    padding: 10px 12px 0 12px;
  }
  .specialization h2 {
    font-size: 16.5px; font-weight: 700; letter-spacing: .3px; margin-bottom: 4px;
  }
  .specialization ul { list-style: none; }
  .specialization li {
    display: flex; gap: 5px;
    font-size: 11.6px; font-weight: 500; text-transform: uppercase; line-height: 17.5px;
  }
  .specialization li svg { flex: none; width: 10px; height: 10px; margin-top: 3px; }
  .specialization .divider {
    width: 270px; height: 2px; margin: 16px auto 0;
    background: linear-gradient(90deg, transparent, #2a0000 20%, #2a0000 80%, transparent);
  }
  .fine-print {
    margin-top: 11px; text-align: center;
    font-size: 9.6px; font-weight: 600; line-height: 1.35; text-transform: uppercase;
  }
</style>
</head>
<body>
<main class="postcard">
  <div class="courtroom-photo" role="img" aria-label="Photo of a wood-panelled courtroom with rows of leather seats and scales of justice"></div>

  <header class="title-box">
    <h1>Dr. K.R. Torrance, Psy.D., NCEB</h1>
    <p>Psychological Evaluator, Board-Certified Forensic Psychologist &amp; National Expert Witness</p>
  </header>

  <section class="signs">
    <h2>4 Signs of a Proficient &amp; Credible Psyc. Expert</h2>
    <div class="sign">
      <svg viewBox="0 0 10 10"><circle cx="5" cy="5" r="4.2" fill="none" stroke="#ec1f27" stroke-width="1.3"/><path d="M3 5.2l1.5 1.5L7.3 3.6" fill="none" stroke="#ec1f27" stroke-width="1.3"/></svg>
      <p><strong>Board Certified by the Continental Council of Courtroom Behavioral Science (CCCB)?</strong> <em>Yes, I'm Board Certified. This mark of proficiency in forensic psychology is recognized by judicial decisions, statutes and regulations.</em></p>
    </div>
    <div class="sign">
      <svg viewBox="0 0 10 10"><circle cx="5" cy="5" r="4.2" fill="none" stroke="#ec1f27" stroke-width="1.3"/><path d="M3 5.2l1.5 1.5L7.3 3.6" fill="none" stroke="#ec1f27" stroke-width="1.3"/></svg>
      <p><strong>Fellow of the Cont. Fellowship of Legal Behavioral Study?</strong> <em>Yes, I'm a CFLB Fellow, along with some of the field's most prominent leaders, comprising the academic arm of the CCCB.</em></p>
    </div>
    <div class="sign">
      <svg viewBox="0 0 10 10"><circle cx="5" cy="5" r="4.2" fill="none" stroke="#ec1f27" stroke-width="1.3"/><path d="M3 5.2l1.5 1.5L7.3 3.6" fill="none" stroke="#ec1f27" stroke-width="1.3"/></svg>
      <p><strong>A Recognized Leader Amongst Other Experts?</strong> <em>I'm the 2018 duly elected President of the Hudson Valley Behavioral Guild Section on Courtroom Assessment, and a Board Member of the Coalition of Practitioners for Youth Safeguarding.</em></p>
    </div>
    <div class="sign">
      <svg viewBox="0 0 10 10"><circle cx="5" cy="5" r="4.2" fill="none" stroke="#ec1f27" stroke-width="1.3"/><path d="M3 5.2l1.5 1.5L7.3 3.6" fill="none" stroke="#ec1f27" stroke-width="1.3"/></svg>
      <p><strong>Positioned in Roles of Trust and Neutrality by Judges?</strong> <em>Yes, I'm an in-house Harborview Juvenile Tribunal mental-health expert for proceedings regarding competency, imminent risk, sentencing, custody, child maltreatment and TPR.</em></p>
    </div>
  </section>

  <footer class="cta-bar">
    Visit <span class="accent">http://offer.witnessbench-example.com</span> or Call <span class="accent">555-014-2937.</span>
  </footer>

  <aside class="specialization">
    <h2>AREAS OF SPECIALIZATION</h2>
    <ul>
      <li><svg viewBox="0 0 10 10"><path d="M1 5.5l2.7 2.7L9 1.8" fill="none" stroke="#fff" stroke-width="1.8"/></svg>CPS &amp;Matrimonial Issues</li>
      <li><svg viewBox="0 0 10 10"><path d="M1 5.5l2.7 2.7L9 1.8" fill="none" stroke="#fff" stroke-width="1.8"/></svg>Competency</li>
      <li><svg viewBox="0 0 10 10"><path d="M1 5.5l2.7 2.7L9 1.8" fill="none" stroke="#fff" stroke-width="1.8"/></svg>Juvenile Delinquency</li>
      <li><svg viewBox="0 0 10 10"><path d="M1 5.5l2.7 2.7L9 1.8" fill="none" stroke="#fff" stroke-width="1.8"/></svg>Criminal Sentencing</li>
      <li><svg viewBox="0 0 10 10"><path d="M1 5.5l2.7 2.7L9 1.8" fill="none" stroke="#fff" stroke-width="1.8"/></svg>Personal Injury and Civil Rights</li>
      <li><svg viewBox="0 0 10 10"><path d="M1 5.5l2.7 2.7L9 1.8" fill="none" stroke="#fff" stroke-width="1.8"/></svg>Immigration</li>
      <li><svg viewBox="0 0 10 10"><path d="M1 5.5l2.7 2.7L9 1.8" fill="none" stroke="#fff" stroke-width="1.8"/></svg>Fitness for Duty, SSD and Workers Comp</li>
      <li><svg viewBox="0 0 10 10"><path d="M1 5.5l2.7 2.7L9 1.8" fill="none" stroke="#fff" stroke-width="1.8"/></svg>Sex-Offenders</li>
      <li><svg viewBox="0 0 10 10"><path d="M1 5.5l2.7 2.7L9 1.8" fill="none" stroke="#fff" stroke-width="1.8"/></svg>IME and Neuropsychological Testing</li>
      <li><svg viewBox="0 0 10 10"><path d="M1 5.5l2.7 2.7L9 1.8" fill="none" stroke="#fff" stroke-width="1.8"/></svg><span>Behind-the-Scenes Consulting on a<br>Contingency Fee</span></li>
      <li><svg viewBox="0 0 10 10"><path d="M1 5.5l2.7 2.7L9 1.8" fill="none" stroke="#fff" stroke-width="1.8"/></svg>Low-Price Initial Screening Evaluations</li>
      <li><svg viewBox="0 0 10 10"><path d="M1 5.5l2.7 2.7L9 1.8" fill="none" stroke="#fff" stroke-width="1.8"/></svg><span>Therapy Services and Programs for<br>Litigants</span></li>
    </ul>
    <div class="divider"></div>
    <p class="fine-print">Fenwick and Torrance, LLC. 2018 New York Licensed<br>Psychologist Lic. # 047213 - New Jersey<br>Licensed Psychologist Lic. # 72K900315847</p>
  </aside>
</main>
</body>
</html>
```